Newsletter design for USA magazine

The four-page newsletter in the middle of our monthly magazine publication needs an accomplished designer to give it a fresh and updated look and feel. The magazine is a trade publication with a mix of lifestyle articles (gardening, outdoors, recipes, etc.) and information about the electric industry. We print 17 versions of the magazine each month, each with its separate and unique four-page newsletter. While some of the elements are the same in each version, the content can vary greatly.
We are looking for a designer to make a base template of the four pages on which we can build, depending on the content we get each month. There needs to be a consistent and similar feel to the rest of the magazine. We are especially interested in new treatment ideas for photos and graphics, and interested in adding embellishments.
You have available a PDF of the magazine to see how the newsletter on pages 7-10 fits in, a recent newsletter to see how it is currently designed and a .zip file of all the original content you will need for the redesign.
Please use the same fonts we use for the magazine, which are Agenda and Minion Pro. If you do not have these fonts available, please use something similar.

```html
<!DOCTYPE html>
<html lang="en">
<head>
<meta charset="utf-8">
<title>Newsletter – From the GM's Desk</title>
<link href="https://fonts.googleapis.com/css2?family=Source+Sans+3:wght@300;400;600;700&family=Crimson+Text:ital,wght@0,400;0,600;1,400&display=swap" rel="stylesheet">
<style>
:root{
  --bg:#d4d4d4;
  --paper:#ffffff;
  --ink:#1e1e1e;
  --navy:#1b2f78;
  --navy-dark:#14235c;
  --magenta:#c8197f;
  --teal:#46c0b8;
  --gold:#f6c75a;
  --rule:#b9b9b9;
  --sans:"Source Sans 3",Arial,sans-serif;
  --serif:"Crimson Text",Georgia,serif;
}
*{margin:0;padding:0;box-sizing:border-box}
html,body{width:1187px;height:1200px;overflow:hidden;background:var(--bg)}
.page{position:absolute;left:191px;top:0;width:804px;height:1200px;background:var(--paper);overflow:hidden}
.photo{position:absolute}
.photo--thermostat{left:0;top:0;width:127px;height:212px;background:linear-gradient(135deg,#d9d4c6,#b8ad93 60%,#d9a23c)}
.photo--children{left:127px;top:0;width:288px;height:212px;background:linear-gradient(160deg,#6f8a3a,#a3a554 45%,#8a6a32)}
.photo--lightning{left:415px;top:0;width:161px;height:212px;background:linear-gradient(170deg,#5a4f93,#9d95d2 50%,#3d3f72)}
.photo--horses{left:576px;top:0;width:228px;height:212px;background:linear-gradient(180deg,#5a94d6,#a9c6e4 40%,#c8a45e 62%,#9b7a3d)}
.brand-bar{position:absolute;left:415px;top:22px;width:389px;height:46px;background:var(--gold);display:flex;align-items:center;padding-left:12px;gap:10px}
.brand-bar__square{width:22px;height:22px;background:var(--navy)}
.brand-bar__name{font:400 22px/1 var(--sans);color:var(--navy);letter-spacing:.3px}
.masthead{position:absolute;left:0;top:212px;width:804px;height:230px}
.masthead svg{position:absolute;left:0;top:0}
.section-title{position:absolute;left:170px;top:225px;font:300 31px/1 var(--sans);color:#fff}
.section-tag{position:absolute;left:520px;top:222px;font:400 15px/1 var(--sans);color:#fff;letter-spacing:.3px}
.portrait{position:absolute;left:40px;top:214px;width:114px;height:140px;background:linear-gradient(180deg,#7c8a6a,#5a5a4e 55%,#2b2f3c)}
.byline{position:absolute;left:170px;top:341px;font:400 12px/1 var(--sans);color:var(--ink);text-transform:uppercase}
.byline b{font-weight:700}
.column{position:absolute;font:400 12px/18px var(--serif);letter-spacing:-.1px;color:var(--ink);text-align:justify;hyphens:auto;overflow:hidden}
.column p{text-indent:12px}
.column p.lead{text-indent:0}
.column--one{left:43px;top:402px;width:190px;height:756px}
.column--two{left:357px;top:402px;width:189px;height:316px}
.column--three{left:566px;top:402px;width:189px;height:316px}
.dropcap{float:left;width:58px;height:58px;border-radius:50%;background:var(--navy);color:#fff;font:700 56px/58px var(--serif);text-align:center;margin:2px 8px 0 0}
.rule{position:absolute;top:402px;width:1px;height:312px;background:var(--rule)}
.rule--a{left:252px}
.rule--b{left:335px}
.pet{position:absolute;left:252px;top:752px;width:552px;height:405px;overflow:hidden}
.pet__photo{position:absolute;inset:0;background:linear-gradient(100deg,#4a4a4a,#7d7870 35%,#e6d6b5 55%,#8a8f9c 80%,#6b5a86)}
.pet svg{position:absolute;left:0;top:0}
.pet__title{position:absolute;left:24px;top:200px;font:700 26px/28px var(--sans);color:#fff}
.pet__title span{font-weight:400}
.pet__name{position:absolute;left:24px;top:290px;font:400 34px/1 var(--sans);color:var(--navy)}
.pet__owner{position:absolute;left:24px;top:362px;font:400 15px/1 var(--sans);color:#fff}
</style>
</head>
<body>
<main class="page">
  <div class="photo photo--thermostat" role="img" aria-label="Hand adjusting a wall thermostat"></div>
  <div class="photo photo--children" role="img" aria-label="Three children tossing autumn leaves outdoors"></div>
  <div class="photo photo--lightning" role="img" aria-label="Lightning bolt in a purple sky"></div>
  <div class="photo photo--horses" role="img" aria-label="Horses running in a meadow"></div>
  <div class="brand-bar"><span class="brand-bar__square"></span><span class="brand-bar__name">RIDGELINE VALLEY ELECTRIC, INC.</span></div>

  <div class="masthead">
    <svg width="804" height="230" viewBox="0 0 804 230">
      <polygon points="0,2 476,2 516,64 0,64" fill="var(--magenta)"/>
      <rect x="16" y="22" width="22" height="22" fill="var(--navy-dark)"/>
      <polygon points="470,2 804,2 804,39 492,39" fill="var(--navy)"/>
      <polygon points="610,39 804,39 804,208" fill="var(--teal)"/>
    </svg>
  </div>
  <div class="portrait" role="img" aria-label="Portrait of the general manager"></div>
  <div class="section-title">From the GM's Desk</div>
  <div class="section-tag">[ RIDGELINE VALLEY ELECTRIC ]</div>
  <div class="byline">By <b>Dale Whitcomb</b> General Manager</div>

  <div class="column column--one">
    <p class="lead"><span class="dropcap">O</span>ctober reminds me of Everett – Everett Hollis, that is, not his pop-smart namesake Mr. Popwell. I remember Hollis because, back in the day, I had to memorize his name for a quiz in freshman citizen class. Everett Hollis: U.S. Secretary of Agriculture under President Carlow. His name never comes up when I play trivia. But as irony has it, he relates to my present-day job as general manager at Ridgeline Valley Electric.</p>
    <p>Back in 1964, Secretary Hollis proclaimed October as the National Co-op Month. The news didn't make the splash the Larkspurs did after appearing on the <i>Evening Variety Hour</i>. Still, Hollis's proclamation mattered to rural America. There, outside of urban population centers, lives markedly improved in two decades, thanks to co-ops with the help of the federal government. Now there was rural electrification. Rural communications. Rural water systems. And the infrastructure to make rural areas comparable to their city cousins was no longer a dream. By 1964, life was no longer the struggle it once was. It no longer felt like rural folks were working <i>Seven Nights a Week</i> (another Larkspurs shout out for you maniacs). National Co-op Month was a deliberate act to encourage us to remember and give thanks. Many of the entities that brought these</p>
  </div>
  <div class="rule rule--a"></div>
  <div class="rule rule--b"></div>
  <div class="column column--two">
    <p class="lead">changes to the countryside were formed as cooperatives: not-for-profit organizations, created solely to provide service. Organizations like Ridgeline Valley Electric, Inc. – still here today, still owned by those we serve, only doing more today than just keeping the lights on.</p>
    <p>This October marks the 53<sup>rd</sup> National Co-op Month. And if you ask me, Everett's proclamation is still the best idea since a pocket on a shirt. The theme this year is "Cooperatives Commit." RVE embodies this theme through its continuing support of local Chambers of Commerce, by</p>
  </div>
  <div class="column column--three">
    <p class="lead">sponsoring and participating in a variety of local events, by awarding Charitable Trust grants funded through Community Roundup, by awarding college scholarships, with Educational Trust grants, by providing safety demonstrations and school science fair trophies, and by supporting of the North Basin and Middle Basin Fairs, the Extra Innings Program and renewable energy installations throughout our service territory.</p>
    <p>Thanks for teeing that up for us, Everett. I'll do my part to keep the month special, <i>With a Little Help from My (Co-op) Neighbors.</i></p>
  </div>

  <section class="pet">
    <div class="pet__photo" role="img" aria-label="Golden retriever puppy beside a hanging flower basket"></div>
    <svg width="552" height="405" viewBox="0 0 552 405">
      <polygon points="0,0 80,0 360,405 0,405" fill="var(--navy)" opacity=".92"/>
      <polygon points="0,160 250,405 0,405" fill="var(--navy-dark)" opacity=".6"/>
      <g fill="var(--gold)">
        <circle cx="30" cy="100" r="7"/><circle cx="22" cy="88" r="3"/><circle cx="30" cy="84" r="3"/><circle cx="38" cy="88" r="3"/>
        <circle cx="58" cy="128" r="7"/><circle cx="50" cy="116" r="3"/><circle cx="58" cy="112" r="3"/><circle cx="66" cy="116" r="3"/>
      </g>
      <polygon points="14,280 128,280 112,302 128,324 14,324" fill="var(--gold)"/>
    </svg>
    <div class="pet__title">PET <span>OF</span><br>THE MONT</div>
    <div class="pet__name">Koda</div>
    <div class="pet__owner">Glen and Mara Whitby's dog</div>
  </section>
</main>
</body>
</html>
```